Zuvex Template Design in Baby Category

We are a maternity/Nestling on Zuvex in need of a store front design template (Store front, listing and detail page page) that is accustom to our category, is user friendly, easy to read and navigate and mobile friendly.

The design should be reflecting a motherhood warm feeling with a modern look.

Please don't hesitate to inquire, if you need any clarification.

Thank you

Industry/Entity Type

Baby

Number of Pages Required

3 page

```html
<!DOCTYPE html>
<html lang="en">
<head>
<meta charset="utf-8">
<title>Nestling – Baby Store Front</title>
<link rel="stylesheet" href="https://fonts.googleapis.com/css2?family=Open+Sans:wght@400;600;700&family=Rajdhani:wght@500;600;700&display=swap">
<style>
:root{
  --red:#e8141b;
  --red-dark:#b80d12;
  --ink:#222;
  --muted:#666;
  --dark:#262626;
  --darker:#1c1c1c;
  --light:#e9e9eb;
  --panel:#f5f5f5;
  --line:#dcdcdc;
  --white:#fff;
  --footer-text:#9a9a9a;
}
*{box-sizing:border-box;margin:0;padding:0}
html,body{width:812px;height:1200px;overflow:hidden}
body{font-family:"Open Sans",Arial,sans-serif;color:var(--ink);background:var(--light);position:relative}
h1,h2,h3{font-weight:400}
.abs{position:absolute}
.head-font{font-family:"Rajdhani","Arial Narrow",sans-serif}

/* header */
.topbar{left:0;top:0;width:812px;height:43px;background:linear-gradient(#2e2e2e,#252525)}
.navbar{left:72px;top:43px;width:670px;height:29px;background:linear-gradient(#474747,#353535);border-radius:3px 3px 0 0}
.nav-item{position:absolute;top:0;height:29px;width:79px;line-height:29px;text-align:center;color:#ddd;font-size:8.5px;letter-spacing:.2px;border-left:1px solid #2a2a2a}
.newsbar{left:0;top:72px;width:812px;height:29px;background:var(--darker)}
.news-text{left:209px;top:81px;font-size:8px;color:#aaa}
.cart-text{right:92px;top:81px;font-size:8px;color:#aaa;white-space:nowrap}
.cart-text b{color:#fff;font-size:10px}
.cart-btn{left:726px;top:79px;width:16px;height:14px;background:var(--red);border-radius:2px}
.logo{left:86px;top:0;width:107px;height:106px;background:linear-gradient(var(--red),var(--red-dark));box-shadow:0 2px 6px rgba(0,0,0,.4);display:flex;align-items:center;justify-content:center}
.logo span{color:var(--white);font-weight:700;font-size:21px}
.social{top:12px;width:18px;height:18px;border-radius:50%;background:#444;border:1px solid #555}
.search{left:620px;top:12px;width:120px;height:17px;border-radius:9px;background:#1a1a1a;border:1px solid #444;font-size:7.5px;color:#bbb;padding:3px 10px}

/* hero */
.hero{left:0;top:101px;width:812px;height:240px;background:linear-gradient(135deg,#dcdde0,#f0f0f2 45%,#dedfe2)}
.hero-photo{left:126px;top:106px;width:192px;height:242px;background:radial-gradient(ellipse at 50% 45%,#f08a9a,#e7c8bc 55%,rgba(233,233,235,0) 72%)}
.hero-title{left:421px;top:144px;font-size:23px;font-weight:500;color:#222}
.hero-copy{left:421px;top:178px;width:266px;font-size:7.6px;line-height:11px;color:#555}
.shop-btn{left:421px;top:262px;width:101px;height:28px;border-radius:3px;background:linear-gradient(#f0282e,var(--red-dark));color:#fff;font-size:11px;line-height:28px;padding-left:14px}
.shop-btn i{position:absolute;right:0;top:0;width:26px;height:28px;border-left:1px solid #c21016}
.arrow-circle{width:36px;height:36px;border-radius:50%;background:linear-gradient(#f3f3f3,#c9c9c9);border:2px solid #fff;box-shadow:0 1px 3px rgba(0,0,0,.3)}

/* featured */
.featured{left:72px;top:335px;width:151px;height:227px;background:var(--white);box-shadow:0 1px 4px rgba(0,0,0,.15)}
.featured-head{left:72px;top:335px;width:151px;height:32px;background:linear-gradient(#f0262c,var(--red-dark));color:#fff;font-size:14px;font-weight:700;padding:7px 14px;letter-spacing:.3px}
.feat-photo{left:86px;top:384px;width:122px;height:116px;background:linear-gradient(135deg,#111,#2a2a2a 50%,#6aa23a 80%,#222)}
.small-title{font-size:7.5px;font-weight:700;color:#222}
.price{font-size:8.5px;color:var(--red)}
.old{font-size:8.5px;color:#999;text-decoration:line-through;margin-left:8px}
.cart-sq{width:24px;height:24px;border-radius:3px;background:linear-gradient(#f0262c,var(--red-dark))}

/* new products */
.newprod{left:223px;top:347px;width:519px;height:215px;background:var(--panel);box-shadow:0 1px 4px rgba(0,0,0,.15)}
.newprod-head{left:237px;top:355px;font-size:12.5px;color:#222}
.newprod-line{left:223px;top:377px;width:519px;height:1px;background:var(--line)}
.card{top:397px;width:154px;height:93px;background:var(--white);border:1px solid #e2e2e2;overflow:hidden}
.card-img{position:absolute;left:35px;top:8px;width:84px;height:76px;border-radius:6px}
.ribbon{position:absolute;right:-20px;top:8px;width:70px;height:13px;background:var(--red);transform:rotate(45deg);color:#fff;font-size:7px;text-align:center;line-height:13px}
.scroll{left:244px;top:539px;width:482px;height:6px;border-radius:3px;background:#e0e0e0}
.scroll-thumb{left:244px;top:537px;width:60px;height:10px;border-radius:5px;background:var(--red)}

/* trending */
.trend-side{left:72px;top:569px;width:151px;height:319px;background:var(--white)}
.trend-head{left:72px;top:569px;width:151px;height:45px;background:#1d1d1d;color:#fff;font-size:13.5px;font-weight:700;padding:14px 14px;letter-spacing:.3px}
.trend-item{left:72px;width:151px;height:34px;line-height:34px;padding-left:14px;font-size:11.5px;color:#333;border-bottom:1px solid #ececec}
.trend-active{left:66px;top:614px;width:157px;height:32px;background:linear-gradient(#ef262c,var(--red-dark));color:#fff;line-height:32px;padding-left:20px;font-size:12px}
.tile{width:259px;height:159px;background:linear-gradient(#fafafa,#ececec);border:1px solid #ddd;overflow:hidden}
.tile-img{position:absolute;left:16px;top:14px;width:115px;height:130px;border-radius:8px}
.tile-name{position:absolute;left:146px;top:30px;font-size:12px;color:#222}
.tile-copy{position:absolute;left:146px;top:49px;width:90px;font-size:7.5px;line-height:11px;color:#777}
.tile-price{position:absolute;left:146px;top:82px}
.add-btn{position:absolute;left:146px;top:107px;width:80px;height:24px;border-radius:3px;background:linear-gradient(#fff,#e3e3e3);border:1px solid #ccc;font-size:7.5px;font-weight:700;line-height:22px;padding-left:33px;color:#222}
.add-btn i{position:absolute;left:-1px;top:-1px;width:24px;height:24px;background:linear-gradient(#f0262c,var(--red-dark));border-radius:3px 0 0 3px}

/* footer */
.footer{left:0;top:888px;width:812px;height:278px;background:linear-gradient(#2a2a2a,#222)}
.partners{left:72px;top:889px;width:670px;height:71px;background:var(--white);border-radius:0 0 4px 4px;box-shadow:0 2px 4px rgba(0,0,0,.3)}
.badge{top:910px;height:30px;border-radius:4px;background:#4a4a4a}
.foot-head{top:983px;font-size:14px;color:#ddd}
.foot-copy{left:72px;top:1013px;width:188px;font-size:7px;line-height:11px;color:var(--footer-text)}
.contact{left:92px;font-size:7.5px;color:#aaa}
.cat-link{font-size:7px;color:#aaa;width:60px;padding-bottom:9px;border-bottom:1px solid #444}
.tweet-ico{left:530px;width:28px;height:28px;border-radius:50%;background:#3c3c3c}
.tweet{left:574px;width:170px;font-size:7px;line-height:10.5px;color:#aaa}
.tweet span{color:#777}
.bottombar{left:0;top:1166px;width:812px;height:34px;background:#161616}
.copyright{left:72px;top:1179px;font-size:7px;color:#888}
.bottom-links{left:551px;top:1179px;font-size:7.5px;color:#aaa;display:flex;gap:13px;white-space:nowrap}
.totop{left:756px;top:1157px;width:34px;height:34px;border-radius:4px;background:linear-gradient(#fff,#d5d5d5);border:1px solid #bbb}
</style>
</head>
<body>

<!-- Header -->
<div class="abs topbar"></div>
<div class="abs social" style="left:465px"></div>
<div class="abs social" style="left:492px"></div>
<div class="abs social" style="left:516px"></div>
<div class="abs social" style="left:543px"></div>
<div class="abs social" style="left:568px"></div>
<div class="abs social" style="left:593px"></div>
<div class="abs search">Search
  <svg class="abs" style="right:8px;top:3px" width="9" height="9" viewBox="0 0 9 9"><circle cx="5.5" cy="3.5" r="2.7" fill="none" stroke="#ccc" stroke-width="1.1"/><line x1="3.5" y1="5.5" x2="1" y2="8" stroke="#ccc" stroke-width="1.3"/></svg>
</div>
<nav class="abs navbar">
  <div class="nav-item" style="left:134px">ENTERAIMENT</div>
  <div class="nav-item" style="left:213px">BODYSUITS</div>
  <div class="nav-item" style="left:292px">BEDDING</div>
  <div class="nav-item" style="left:371px">ENTERAIMENT</div>
  <div class="nav-item" style="left:450px">TOYS</div>
  <div class="nav-item" style="left:529px">BATHING</div>
</nav>
<div class="abs newsbar"></div>
<div class="abs news-text">October. 12. 2015 - Syrian prime minister defects, fighting goes on</div>
<div class="abs cart-text">Shopping Cart: <b>0</b> item(s) - $0.00</div>
<div class="abs cart-btn"><svg width="16" height="14" viewBox="0 0 16 14"><path d="M5 5h6l-3 4z" fill="#fff"/></svg></div>
<div class="abs logo"><span>Nestling</span></div>

<!-- Hero -->
<section class="abs hero"></section>
<div class="abs hero-photo" role="img" aria-label="Toddler in a pink dress taking a step"></div>
<h1 class="abs hero-title head-font">Where can I get some?</h1>
<p class="abs hero-copy">Fusce ultrices ornare velit, consectetur tempus eros dapibus et. Integer lobortis, dui in iaculis sollicitudin, felis nunc aliquam nibh, eu porta nisi urna nec odio. Duis suscipit viverra magna id sagittis. Quisque odio neque, condimentum cursus volutpat vel, pharetra ac nibh. Cras cursus libero id nunc facilisis luctus. Aenean ultricies, risus cursus sollicitudin congue, diam diam congue velit, ut sodales sem enim a nisl. Aenean elit diam, mollis fermentum</p>
<div class="abs shop-btn">Shop Now<i><svg width="26" height="28" viewBox="0 0 26 28"><path d="M8 11h5V7l6 7-6 7v-4H8z" fill="#fff"/></svg></i></div>
<div class="abs arrow-circle" style="left:34px;top:202px"><svg width="32" height="32" viewBox="0 0 32 32"><path d="M19 9l-7 7 7 7" fill="none" stroke="#888" stroke-width="2.5"/></svg></div>
<div class="abs arrow-circle" style="left:743px;top:202px"><svg width="32" height="32" viewBox="0 0 32 32"><path d="M13 9l7 7-7 7" fill="none" stroke="#888" stroke-width="2.5"/></svg></div>

<!-- Featured -->
<div class="abs featured"></div>
<div class="abs featured-head head-font">FEATURED
  <svg class="abs" style="right:12px;top:10px" width="24" height="12" viewBox="0 0 24 12"><path d="M7 1L2 6l5 5M17 1l5 5-5 5" fill="none" stroke="#fff" stroke-width="2"/></svg>
</div>
<div class="abs feat-photo" role="img" aria-label="Baby in green shirt playing with stacking rings"></div>
<div class="abs small-title" style="left:86px;top:507px">Herbal Sport</div>
<div class="abs" style="left:86px;top:523px"><span class="price">$101.88</span><span class="old">$69.99</span></div>
<div class="abs cart-sq" style="left:185px;top:512px"><svg width="24" height="24" viewBox="0 0 24 24"><path d="M6 8h2l2 7h6l2-5H9" fill="none" stroke="#fff" stroke-width="1.4"/><circle cx="11" cy="17.5" r="1" fill="#fff"/><circle cx="15.5" cy="17.5" r="1" fill="#fff"/></svg></div>

<!-- New products -->
<section class="abs newprod"></section>
<h2 class="abs newprod-head">NEW PRODUCTS</h2>
<div class="abs newprod-line"></div>

<div class="abs card" style="left:238px"><div class="card-img" role="img" aria-label="Colourful wooden hammer toy" style="background:radial-gradient(circle,#3fb3d6,#f2c230 55%,#fff 75%)"></div><div class="ribbon">Sale</div></div>
<div class="abs small-title" style="left:238px;top:498px">Lorem ipsum dolor sit</div>
<div class="abs" style="left:238px;top:513px"><span class="old" style="margin:0 8px 0 0">$69.99</span><span class="price">$34.99</span></div>
<div class="abs cart-sq" style="left:367px;top:499px"><svg width="24" height="24" viewBox="0 0 24 24"><path d="M6 8h2l2 7h6l2-5H9" fill="none" stroke="#fff" stroke-width="1.4"/><circle cx="11" cy="17.5" r="1" fill="#fff"/><circle cx="15.5" cy="17.5" r="1" fill="#fff"/></svg></div>

<div class="abs card" style="left:406px"><div class="card-img" role="img" aria-label="Orange plush puppet toy" style="background:radial-gradient(circle,#f39a2b,#2f78c4 50%,#fff 75%)"></div></div>
<div class="abs small-title" style="left:406px;top:498px">Lorem ipsum dolor sit</div>
<div class="abs price" style="left:406px;top:513px">$34.99</div>
<div class="abs cart-sq" style="left:535px;top:499px"><svg width="24" height="24" viewBox="0 0 24 24"><path d="M6 8h2l2 7h6l2-5H9" fill="none" stroke="#fff" stroke-width="1.4"/><circle cx="11" cy="17.5" r="1" fill="#fff"/><circle cx="15.5" cy="17.5" r="1" fill="#fff"/></svg></div>

<div class="abs card" style="left:574px"><div class="card-img" role="img" aria-label="Brown teddy bear" style="background:radial-gradient(circle,#b07a3e,#d8b07a 50%,#fff 75%)"></div></div>
<div class="abs small-title" style="left:574px;top:498px">Lorem ipsum dolor sit</div>
<div class="abs price" style="left:574px;top:513px">$34.99</div>
<div class="abs cart-sq" style="left:703px;top:499px"><svg width="24" height="24" viewBox="0 0 24 24"><path d="M6 8h2l2 7h6l2-5H9" fill="none" stroke="#fff" stroke-width="1.4"/><circle cx="11" cy="17.5" r="1" fill="#fff"/><circle cx="15.5" cy="17.5" r="1" fill="#fff"/></svg></div>

<div class="abs scroll"></div>
<div class="abs scroll-thumb"></div>

<!-- Trending -->
<aside class="abs trend-side"></aside>
<div class="abs trend-head head-font">TRENDING NOW</div>
<div class="abs trend-active">Clothing</div>
<svg class="abs" style="left:223px;top:614px" width="9" height="32" viewBox="0 0 9 32"><path d="M0 0l9 16-9 16z" fill="#cf1117"/></svg>
<div class="abs trend-item" style="top:646px">Toys</div>
<div class="abs trend-item" style="top:680px">Feeding</div>
<div class="abs trend-item" style="top:714px">Bedding</div>

<div class="abs tile" style="left:223px;top:569px">
  <div class="tile-img" role="img" aria-label="Pink baby romper with bow headband" style="background:radial-gradient(circle,#f3a2bb,#9cd3ea 55%,rgba(255,255,255,0) 75%)"></div>
  <div class="ribbon">Sale</div>
  <div class="tile-name">Clothing</div>
  <div class="tile-copy">Lorem ipsum dolor sit amet, consectetuer</div>
  <div class="tile-price"><span class="old" style="margin:0 12px 0 0">$34.99</span><span class="price">$34.99</span></div>
  <div class="add-btn"><i><svg width="24" height="24" viewBox="0 0 24 24"><path d="M6 8h2l2 7h6l2-5H9" fill="none" stroke="#fff" stroke-width="1.4"/><circle cx="11" cy="17.5" r="1" fill="#fff"/><circle cx="15.5" cy="17.5" r="1" fill="#fff"/></svg></i>Add to cart</div>
</div>
<div class="abs tile" style="left:482px;top:569px">
  <div class="tile-img" role="img" aria-label="Green plush dragon toy" style="background:radial-gradient(circle,#7dc242,#e24b8a 50%,rgba(255,255,255,0) 75%)"></div>
  <div class="tile-name">Toys</div>
  <div class="tile-copy">Lorem ipsum dolor sit amet, consectetuer</div>
  <div class="tile-price"><span class="price">$34.99</span></div>
  <div class="add-btn"><i><svg width="24" height="24" viewBox="0 0 24 24"><path d="M6 8h2l2 7h6l2-5H9" fill="none" stroke="#fff" stroke-width="1.4"/><circle cx="11" cy="17.5" r="1" fill="#fff"/><circle cx="15.5" cy="17.5" r="1" fill="#fff"/></svg></i>Add to cart</div>
</div>
<div class="abs tile" style="left:223px;top:728px">
  <div class="tile-img" role="img" aria-label="Baby food jars and cereal boxes" style="background:radial-gradient(circle,#f1d27a,#3a7cc7 55%,rgba(255,255,255,0) 75%)"></div>
  <div class="tile-name">Feeding</div>
  <div class="tile-copy">Lorem ipsum dolor sit amet, consectetuer</div>
  <div class="tile-price"><span class="price">$34.99</span></div>
  <div class="add-btn"><i><svg width="24" height="24" viewBox="0 0 24 24"><path d="M6 8h2l2 7h6l2-5H9" fill="none" stroke="#fff" stroke-width="1.4"/><circle cx="11" cy="17.5" r="1" fill="#fff"/><circle cx="15.5" cy="17.5" r="1" fill="#fff"/></svg></i>Add to cart</div>
</div>
<div class="abs tile" style="left:482px;top:728px">
  <div class="tile-img" role="img" aria-label="Red and black checked infant car seat" style="background:radial-gradient(circle,#c0202a,#1a1a1a 55%,rgba(255,255,255,0) 75%)"></div>
  <div class="tile-name">Bedding</div>
  <div class="tile-copy">Lorem ipsum dolor sit amet, consectetuer</div>
  <div class="tile-price"><span class="price">$34.99</span></div>
  <div class="add-btn"><i><svg width="24" height="24" viewBox="0 0 24 24"><path d="M6 8h2l2 7h6l2-5H9" fill="none" stroke="#fff" stroke-width="1.4"/><circle cx="11" cy="17.5" r="1" fill="#fff"/><circle cx="15.5" cy="17.5" r="1" fill="#fff"/></svg></i>Add to cart</div>
</div>

<!-- Footer -->
<footer class="abs footer"></footer>
<div class="abs partners"></div>
<svg class="abs" style="left:84px;top:917px" width="12" height="16" viewBox="0 0 12 16"><path d="M9 2L3 8l6 6" fill="none" stroke="#999" stroke-width="2"/></svg>
<svg class="abs" style="left:716px;top:917px" width="12" height="16" viewBox="0 0 12 16"><path d="M3 2l6 6-6 6" fill="none" stroke="#999" stroke-width="2"/></svg>
<div class="abs badge" style="left:117px;width:112px"></div>
<div class="abs badge" style="left:250px;width:164px"></div>
<div class="abs badge" style="left:438px;width:118px"></div>
<div class="abs badge" style="left:583px;width:112px"></div>

<h3 class="abs foot-head" style="left:72px">Who We Are</h3>
<p class="abs foot-copy">Lorem Ipsum is simply dummy text of the printing and typesetting industry. Lorem Ipsum has been the industry's standard dummy text ever since the 1500s, when an unknown printer took a galley of type and scrambled it to make a type specimen book. It has</p>
<svg class="abs" style="left:73px;top:1085px" width="10" height="10" viewBox="0 0 10 10"><path d="M1 0v10M1 1h7l-2 2.5 2 2.5H1" fill="var(--red)" stroke="var(--red)"/></svg>
<div class="abs contact" style="top:1086px">14 Willow Lane, Brookvale</div>
<svg class="abs" style="left:73px;top:1106px" width="10" height="10" viewBox="0 0 10 10"><rect x="1" y="1" width="8" height="8" fill="none" stroke="var(--red)" stroke-width="1.5"/></svg>
<div class="abs contact" style="top:1107px">(041) 555-0182</div>
<svg class="abs" style="left:73px;top:1127px" width="10" height="8" viewBox="0 0 10 8"><rect width="10" height="8" fill="var(--red)"/><path d="M0 0l5 4 5-4" fill="none" stroke="#222" stroke-width="1"/></svg>
<div class="abs contact" style="top:1126px">hello@nestlingshop.com</div>

<h3 class="abs foot-head" style="left:300px">Categories</h3>
<div class="abs" style="left:301px;top:1018px">
  <div class="cat-link">New collection</div><div class="cat-link" style="margin-top:10px">Best sellers</div><div class="cat-link" style="margin-top:10px">Manufacturers</div><div class="cat-link" style="margin-top:10px">Suppliers</div><div class="cat-link" style="margin-top:10px">New Products</div>
</div>
<div class="abs" style="left:378px;top:1018px">
  <div class="cat-link">New collection</div><div class="cat-link" style="margin-top:10px">Best sellers</div><div class="cat-link" style="margin-top:10px">Manufacturers</div><div class="cat-link" style="margin-top:10px">Suppliers</div><div class="cat-link" style="margin-top:10px">New Products</div>
</div>
<div class="abs" style="left:455px;top:1018px">
  <div class="cat-link">New collection</div><div class="cat-link" style="margin-top:10px">Best sellers</div><div class="cat-link" style="margin-top:10px">Manufacturers</div><div class="cat-link" style="margin-top:10px">Suppliers</div><div class="cat-link" style="margin-top:10px">New Products</div>
</div>

<h3 class="abs foot-head" style="left:530px">Lastest Tweet</h3>
<div class="abs tweet-ico" style="top:1015px"></div>
<div class="abs tweet" style="top:1015px">Check out this great #craftmart item for you 'Cozy Nursery Kit' http://nst.li/k3w9<br><span>2 hours ago</span></div>
<div class="abs tweet-ico" style="top:1064px"></div>
<div class="abs tweet" style="top:1064px">Check out this great #craftmart item for you 'Cozy Nursery Kit' http://nst.li/k3w9<br><span>2 hours ago</span></div>
<div class="abs tweet-ico" style="top:1112px"></div>
<div class="abs tweet" style="top:1112px">Check out this great #craftmart item for you 'Cozy Nursery Kit' http://nst.li/k3w9<br><span>2 hours ago</span></div>

<div class="abs bottombar"></div>
<div class="abs copyright">Copyrights. © 2015 by NESTLING</div>
<nav class="abs bottom-links"><span>Home</span><span>Toys</span><span>Feeding</span><span>Bedding</span><span>Contact us</span></nav>
<div class="abs totop"><svg width="32" height="32" viewBox="0 0 32 32"><path d="M16 8l8 9h-5v7h-6v-7H8z" fill="#999"/></svg></div>

</body>
</html>
```